Boilerplate Management Organization Chart

"Our Management Approach is a deliberate step-by-step process and supports our Technical Approach detailed in proposal submission. The Management Approach covers all the human capital aspects for executing a contract—from contract award through to sustainment and/or transition of the contract to another company. It includes how we organize, hire, staff, train, and account for our contract employees—as well as their complete personal life-cycle management within the company."

We need this management approach to depict an amazing management process that demonstrates best practices of the project management body of knowledge. We need this vector image to be applicable to any proposal without making references to any other proposals. Generic names but using strong business language.
Updates

Thanks for all designs submitted thus far. Some have stuck to the original type of chart. We would like to see a completely different way to show the same information. It has to be able to be recognized and deciphered very quickly by people who might not necessarily want to look at it. It must draw them in and make it incredibly easy to distinguish a management approach that looks fresh, infallible, and easily implemented.

Target Market(s)

Federal space, Government organizations looking for procedural efficiencies,

Industry/Entity Type

Management

Requirements
Must have
• Must not take up more than 1/3 to 1/2 of printable page and be clear.
Should not have
• Not too much color, but should stick to some color palette of some interest.

```html
<!DOCTYPE html>
<html lang="en">
<head>
<meta charset="UTF-8">
<title>Management Approach — Process Chart</title>
<link rel="stylesheet" href="https://fonts.googleapis.com/css2?family=Montserrat:wght@500&family=Signika:wght@600&display=swap">
<style>
  :root {
    --navy: #03168a;
    --accent: #c4c000;
    --label: #d2d2d2;
    --paper: #ffffff;
  }
  html, body {
    margin: 0;
    padding: 0;
    width: 1200px;
    height: 1200px;
    overflow: hidden;
    background: var(--paper);
  }
  .chart {
    display: block;
    width: 1200px;
    height: 1200px;
  }
  .band { fill: var(--navy); }
  .pointer { fill: var(--accent); filter: url(#soft-shadow); }
  .pillar-title {
    font-family: "Montserrat", Arial, sans-serif;
    font-weight: 500;
    font-size: 104px;
    fill: var(--label);
  }
  .step-label {
    font-family: "Signika", "Trebuchet MS", sans-serif;
    font-weight: 600;
    font-size: 60px;
    fill: var(--label);
    text-anchor: middle;
    filter: url(#text-shadow);
  }
</style>
</head>
<body>
<svg class="chart" viewBox="0 0 1500 1500" xmlns="http://www.w3.org/2000/svg" role="img" aria-label="Management approach process chart">
  <defs>
    <filter id="soft-shadow" x="-20%" y="-20%" width="140%" height="160%">
      <feDropShadow dx="0" dy="4" stdDeviation="4" flood-color="#000" flood-opacity="0.35"/>
    </filter>
    <filter id="text-shadow" x="-5%" y="-20%" width="110%" height="140%">
      <feDropShadow dx="2" dy="2" stdDeviation="1.5" flood-color="#000" flood-opacity="0.5"/>
    </filter>
  </defs>

  <!-- Management approach frame -->
  <path class="band management-frame" d="M208,1398 V118 Q208,28 298,28 H640 V172 H352 V1398 A72,72 0 0 1 208,1398 Z"/>
  <text class="pillar-title" transform="translate(316,1420) rotate(-90)" textLength="1335" lengthAdjust="spacingAndGlyphs">MANAGEMENT APPROACH</text>

  <!-- Program evaluation pillar -->
  <rect class="band evaluation-pillar" x="397" y="213" width="133" height="1267" rx="66.5"/>
  <text class="pillar-title" transform="translate(502,1420) rotate(-90)" textLength="1145" lengthAdjust="spacingAndGlyphs">PROGRAM EVALUATION</text>

  <!-- Process steps -->
  <g class="process-steps">
    <path class="band" d="M608,28 H1203 A72,72 0 0 1 1275,100 V172 H608 Z"/>
    <rect class="band" x="1130" y="170" width="145" height="45"/>
    <path class="band" d="M639,213 H1275 V288 A72,72 0 0 1 1203,360 H567 V285 A72,72 0 0 1 639,213 Z"/>
    <rect class="band" x="567" y="358" width="145" height="41"/>
    <path class="band" d="M567,397 H1203 A72,72 0 0 1 1275,469 V545 H639 A72,72 0 0 1 567,473 Z"/>
    <rect class="band" x="1130" y="543" width="145" height="44"/>
    <path class="band" d="M639,585 H1275 V658 A72,72 0 0 1 1203,730 H567 V657 A72,72 0 0 1 639,585 Z"/>
    <rect class="band" x="567" y="728" width="145" height="44"/>
    <path class="band" d="M567,770 H1203 A72,72 0 0 1 1275,842 V917 H639 A72,72 0 0 1 567,845 Z"/>
    <rect class="band" x="1130" y="915" width="145" height="47"/>
    <path class="band" d="M639,960 H1275 V1033 A72,72 0 0 1 1203,1105 H567 V1032 A72,72 0 0 1 639,960 Z"/>
    <rect class="band" x="567" y="1103" width="145" height="46"/>
    <path class="band" d="M567,1147 H1203 A72,72 0 0 1 1275,1219 V1292 H639 A72,72 0 0 1 567,1220 Z"/>
    <rect class="band" x="1130" y="1290" width="145" height="42"/>
    <path class="band" d="M639,1330 H1275 V1400 A72,72 0 0 1 1203,1472 H639 A72,72 0 0 1 567,1400 V1402 A72,72 0 0 1 639,1330 Z"/>
  </g>

  <!-- Flow pointers -->
  <g class="flow-pointers">
    <polygon class="pointer" points="608,28 668,98 608,172"/>
    <polygon class="pointer" points="1130,185 1275,185 1202,245"/>
    <polygon class="pointer" points="567,373 712,373 638,433"/>
    <polygon class="pointer" points="1130,557 1275,557 1202,617"/>
    <polygon class="pointer" points="567,745 712,745 638,805"/>
    <polygon class="pointer" points="1130,932 1275,932 1202,992"/>
    <polygon class="pointer" points="567,1120 712,1120 638,1180"/>
    <polygon class="pointer" points="1130,1307 1275,1307 1202,1367"/>
  </g>

  <!-- Step labels -->
  <g class="step-labels">
    <text class="step-label" x="920" y="90">Responsibility</text>
    <text class="step-label" x="920" y="154">Fixed</text>
    <text class="step-label" x="920" y="274">Management</text>
    <text class="step-label" x="920" y="339">&amp; Oversight</text>
    <text class="step-label" x="920" y="456">Manning</text>
    <text class="step-label" x="920" y="521">the Team</text>
    <text class="step-label" x="920" y="680">Training</text>
    <text class="step-label" x="920" y="828">Professional</text>
    <text class="step-label" x="920" y="893">Development</text>
    <text class="step-label" x="920" y="1019">Retention/</text>
    <text class="step-label" x="920" y="1085">Quality of Life</text>
    <text class="step-label" x="920" y="1242">Benefits</text>
    <text class="step-label" x="920" y="1385">Sustainment/</text>
    <text class="step-label" x="920" y="1450">Transition</text>
  </g>
</svg>
</body>
</html>
```